Mobile Dental Clinic for Students!!

Hi There!!
I need a marketing email to bring awareness that children need to see a dentist every year to get cleans done!! This email will be going to admin officers, principals etc.
We are a mobile dental provider, and we come to the school in our mobile van!
I have attached the flyer that will be going out to schools next week but wanted to send a marketing email as well
I have included a URL https://brightpathforms.formvault.example/to/kPeRtZ
to go on the marketing email to be included for easy registration for a school.
You can use stock photos~~ aswell
If you need words please copy from the flyer attached.
Also need the following on the marketing email
ph: 1800 7GLOWS
www.toothtrekvan.com.au
info@toothtrekvan.com.au
Thanks and have fun with it!!!
Target Market(s)
principals, teachers, admin staff
Industry/Entity Type
Healthcare

```html
<!DOCTYPE html>
<html lang="en">
<head>
<meta charset="utf-8">
<title>ToothTrek Van – Mobile Dental Clinic for Students</title>
<link rel="stylesheet" href="https://fonts.googleapis.com/css2?family=Dosis:wght@400;500;600;700&display=swap">
<style>
:root{
  --page:#e4e4e4;
  --paper:#ffffff;
  --teal:#1aa68c;
  --orange:#f4702b;
  --navy:#0c5b90;
  --ink:#4f4f4f;
  --heading:#5c5c5c;
  --muted:#9a9a9a;
  --rule:#d3d3d3;
  --link:#1f5fae;
}
*{margin:0;padding:0;box-sizing:border-box}
html,body{width:1200px;height:2594px;overflow:hidden}
body{background:var(--page);font-family:"Dosis",sans-serif;color:var(--ink);position:relative}
a{text-decoration:none;color:inherit}
.abs{position:absolute}
.preheader{top:80px;left:0;width:1200px;text-align:center;font-size:19px;color:#333}
.preheader a{color:var(--link);font-weight:700;text-decoration:underline}
.mail{top:122px;left:225px;width:752px;height:2374px;background:var(--paper);border-top:5px solid var(--orange);border-bottom:5px solid var(--orange)}
.brand{font-weight:700;color:var(--teal);letter-spacing:.5px;display:flex;align-items:center}
.brand--header{top:160px;left:256px;font-size:50px}
.brand--footer{top:2290px;left:0;width:1200px;justify-content:center;font-size:44px}
.social{display:flex;gap:6px}
.social span{width:30px;height:30px;border-radius:50%;background:var(--navy)}
.social--header{top:144px;left:845px}
.social--header span:nth-child(2){background:#1da1d8}
.social--header span:nth-child(3){background:#e3412c}
.date{top:186px;left:758px;display:flex;align-items:center;gap:10px;font-size:24px;font-weight:600;color:#666}
.hero{top:263px;left:256px;width:688px;height:200px;background:linear-gradient(100deg,#cfdbe6 0%,#e9d9cc 45%,#f1f4f6 100%)}
.hero-band{top:463px;left:256px;width:688px;height:90px;background:var(--teal);color:#fff;font-weight:700;font-size:22px;line-height:29px;padding:19px 0 0 29px}
.btn{background:var(--orange);color:#fff;font-weight:700;display:flex;align-items:center;justify-content:center;letter-spacing:.3px}
.btn--visit{top:486px;left:728px;width:202px;height:50px;font-size:20px}
.btn--about{top:807px;left:477px;width:249px;height:52px;font-size:19px}
.btn--more{top:1826px;left:258px;width:147px;height:50px;font-size:17px}
.section-title{left:0;width:1200px;text-align:center;font-weight:600;font-size:31px;color:var(--heading)}
.copy{font-size:18.5px;line-height:27.5px;color:var(--ink)}
.about-copy{top:618px;left:256px;width:650px}
.about-copy p+p{margin-top:27px}
.services{top:911px;left:301px;width:591px;height:202px;border:1.5px solid var(--rule)}
.services h2{position:absolute;top:-22px;left:0;width:100%;text-align:center;font-size:31px;font-weight:600;color:var(--heading)}
.services h2 span{background:var(--paper);padding:0 14px}
.service-list{position:absolute;top:45px;left:66px;display:grid;grid-template-columns:279px 200px;row-gap:18px;list-style:none;font-size:19px}
.dot-item{display:flex;align-items:center;gap:14px}
.dot-item::before{content:"";width:16px;height:16px;border-radius:50%;background:var(--muted);flex:none}
.offers{top:1200px;left:284px;width:640px;list-style:none}
.offers li{display:flex;gap:13px;font-size:18.5px;line-height:25px;margin-bottom:25px}
.offers li::before{content:"";width:16px;height:16px;border-radius:50%;background:var(--muted);flex:none;margin-top:6px}
.divider{top:1499px;left:256px;width:688px;border-top:1.5px dashed var(--rule)}
.cdbs{top:1558px;left:256px;width:430px;font-size:18px;line-height:27.5px}
.cdbs p+p{margin-top:6px}
.call-card{top:1554px;left:702px;width:242px;height:322px;background:var(--navy);overflow:hidden;color:#fff;text-align:center}
.call-card .phone{position:absolute;top:54px;width:100%;font-size:31px;font-weight:500;line-height:36px}
.call-card .web{position:absolute;top:136px;width:100%;font-size:16px;font-weight:600}
.call-card .curve{position:absolute;top:164px;left:-80px;width:402px;height:330px;border-radius:50%;background:var(--orange)}
.call-card .cta{position:absolute;top:198px;left:24px;width:200px;font-size:21px;line-height:27px;text-align:left}
.free{top:1943px;left:258px;width:684px;height:322px;background:linear-gradient(180deg,#23ad96 0%,#1aa68c 100%);color:#fff}
.free h2{position:absolute;top:20px;width:100%;text-align:center;font-size:29px;font-weight:600}
.free ul{position:absolute;top:76px;left:54px;width:590px;list-style:none}
.free li{display:flex;gap:10px;font-size:18.5px;font-weight:600;line-height:22px;margin-bottom:18px}
.free li svg{flex:none;margin-top:3px}
.contacts{top:2388px;left:256px;width:688px;display:flex;justify-content:center;gap:26px;font-size:17px;color:#555}
.contacts a{display:flex;align-items:center;gap:8px;white-space:nowrap}
.footer-rule{top:2434px;left:256px;width:688px;border-top:1.5px solid var(--rule)}
.copyright{top:2450px;left:256px;font-size:19px;color:#555}
.social--footer{top:2446px;left:825px}
.social--footer span{width:34px;height:34px;background:#a8a8a8}
</style>
</head>
<body>
<p class="abs preheader">For anything about this mail you can contract us by <a href="https://brightpathforms.formvault.example/to/kPeRtZ">CLICK THIS LINK.</a></p>

<div class="abs mail"></div>

<div class="abs brand brand--header">ToothTrek Van</div>
<div class="abs social social--header"><span></span><span></span><span></span></div>
<div class="abs date">
  <svg width="30" height="30" viewBox="0 0 30 30" fill="none" stroke="#777" stroke-width="2"><rect x="2" y="5" width="26" height="23"/><line x1="2" y1="11" x2="28" y2="11"/><line x1="9" y1="2" x2="9" y2="7"/><line x1="21" y1="2" x2="21" y2="7"/></svg>
  OCTOBER 7, 2016
</div>

<div class="abs hero" role="img" aria-label="Photo of a child in the dental chair during a check-up with a masked dentist"></div>
<div class="abs hero-band">We are a mobile dental provider, and we come<br>to the school in our mobile van!</div>
<a class="abs btn btn--visit" href="https://www.toothtrekvan.com.au">Visit Our Website</a>

<h2 class="abs section-title" style="top:576px">Who we are?</h2>
<div class="abs copy about-copy">
  <p>ToothTrek Van Dental will offer your school state-of-the art, on-stite oral health care services, including checkups and basic dental care ot your school.</p>
  <p>we endeavour to provide a solution to such. With school and parental consent , we offer students professional, tailored and convenient dental care , utilising the latest technologies and techniques to achive optimum results.</p>
</div>
<a class="abs btn btn--about" href="https://brightpathforms.formvault.example/to/kPeRtZ">Read Details About Us</a>

<section class="abs services">
  <h2><span>OUR SERVICES WE PROVIDE TO STUDENTS</span></h2>
  <ul class="service-list">
    <li class="dot-item">Dental Examinations</li><li class="dot-item">Sealants and x-ray</li>
    <li class="dot-item">Dental Cleaning</li><li class="dot-item">Fillings</li>
    <li class="dot-item">Fluoride Treatment</li><li class="dot-item">Exptractions</li>
  </ul>
</section>

<h2 class="abs section-title" style="top:1145px">We offers?</h2>
<ul class="abs offers">
  <li>Bluk -Billed assessment and treatment to students who qualify for Medicare CDBS program' this includes a dental check-up, cleaning &amp; fluoride treatments, sealants , X-rays and fillings.</li>
  <li>If students are not eligible for the Medicare CDBS Scheme, we offer the student a prevention package of $99 all claimable through their health fund.</li>
  <li>On-on-one Dral Dental education form ou rprofessional Dental Clinicians.</li>
  <li>Complimentary Dental Care Pack comprise of a toothbrush, toothpaste and other products.</li>
</ul>
<div class="abs divider"></div>

<div class="abs cdbs">
  <p>ToothTrek Van will take the trouble of visiting the dentist by bringing our dentists to your school in a van similar to Wellness Wally!</p>
  <p>Under the Child Dental Benefits Scheme (CDBS) This Scheme is administered by the Department fo Human Sevices under Medicare. The program commenced on 1 January 2014 and provided acess to benefits for basic dental services to around 3.4 million children agedd 2-17 years.......</p>
</div>
<a class="abs btn btn--more" href="https://brightpathforms.formvault.example/to/kPeRtZ">READ MORE</a>

<aside class="abs call-card">
  <svg style="position:absolute;top:12px;left:104px" width="34" height="34" viewBox="0 0 34 34" fill="none" stroke="#fff" stroke-width="2"><circle cx="17" cy="17" r="15"/><path d="M12 10l3 3-2 2c1 3 3 5 6 6l2-2 3 3-2 3c-6-1-11-6-12-12z"/></svg>
  <div class="phone">1800 7GLOWS</div>
  <svg style="position:absolute;top:100px;left:108px" width="26" height="26" viewBox="0 0 30 30" fill="none" stroke="#fff" stroke-width="3"><path d="M24 12a10 10 0 0 0-18-3"/><path d="M6 18a10 10 0 0 0 18 3"/><path d="M4 4v6h6M26 26v-6h-6"/></svg>
  <div class="web">www.toothtrekvan.com.au</div>
  <div class="curve"></div>
  <a class="cta" href="https://brightpathforms.formvault.example/to/kPeRtZ">Give us a call today on 1800 7GLOWS to book the Dental Clinic to come to yoru school!</a>
</aside>

<section class="abs free" role="img" aria-label="Soft teal backdrop of happy school children">
  <h2>Free to the school</h2>
  <ul>
    <li><svg width="18" height="16" viewBox="0 0 18 16" fill="none" stroke="#fff" stroke-width="2.5"><path d="M2 9l5 5L16 2"/></svg>Parents are Bulked Billed through Medicare for students's treatment.</li>
    <li><svg width="18" height="16" viewBox="0 0 18 16" fill="none" stroke="#fff" stroke-width="2.5"><path d="M2 9l5 5L16 2"/></svg>we bring the entire dental practice and Dentists to your school.</li>
    <li><svg width="18" height="16" viewBox="0 0 18 16" fill="none" stroke="#fff" stroke-width="2.5"><path d="M2 9l5 5L16 2"/></svg>One on one education sessions tailored to each student.</li>
    <li><svg width="18" height="16" viewBox="0 0 18 16" fill="none" stroke="#fff" stroke-width="2.5"><path d="M2 9l5 5L16 2"/></svg>we encourage better oral hygiene and can provide further treatment if necessary.</li>
    <li><svg width="18" height="16" viewBox="0 0 18 16" fill="none" stroke="#fff" stroke-width="2.5"><path d="M2 9l5 5L16 2"/></svg>prevention-focused.</li>
  </ul>
</section>

<div class="abs brand brand--footer">ToothTrek Van</div>
<div class="abs contacts">
  <a href="https://www.toothtrekvan.com.au"><svg width="28" height="28" viewBox="0 0 30 30" fill="none" stroke="#666" stroke-width="1.6"><circle cx="15" cy="15" r="13"/><ellipse cx="15" cy="15" rx="6" ry="13"/><line x1="2" y1="15" x2="28" y2="15"/><line x1="4" y1="8" x2="26" y2="8"/><line x1="4" y1="22" x2="26" y2="22"/></svg>www.toothtrekvan.com.au</a>
  <a href="tel:18007456977"><svg width="28" height="28" viewBox="0 0 34 34" fill="none" stroke="#666" stroke-width="1.8"><circle cx="17" cy="17" r="15"/><path d="M12 10l3 3-2 2c1 3 3 5 6 6l2-2 3 3-2 3c-6-1-11-6-12-12z"/></svg>1800 7GLOWS</a>
  <a href="mailto:info@toothtrekvan.com.au"><svg width="28" height="28" viewBox="0 0 30 30" fill="none" stroke="#666" stroke-width="1.6"><circle cx="15" cy="15" r="13"/><rect x="8" y="10" width="14" height="10"/><path d="M8 10l7 6 7-6"/></svg>info@toothtrekvan.com.au</a>
</div>
<div class="abs footer-rule"></div>
<p class="abs copyright">Copyright 2016 by ToothTrek Van. All right reserved by the Company.</p>
<div class="abs social social--footer"><span></span><span></span><span></span></div>
</body>
</html>
```